Design a WordPress w/ woocommerce Plugin - Website for www.plan-sheetcraft.example

Quick Steps
I would like an easy way for a pool company to come to my site, fill in a form (WEB page form) and select from three packages, buy then use a link to go to a site to upload and collaborate.

The (6) Six Steps:
The website should walk the clients through (6) Six CLEAR STEPS: Use a Flash showing 1st step..... Flash 2nd Step... Flash 3rd step etc..... Up to Flash 6th Step...
1. Introduce the client to the service I provide (Plansheet Craft used to build pools in DRAFO or PLANMAKR formats)
a. The client has unlimited changes
b. Money back guarantee
2. Client fills out a form giving me information about the project. Including drop downs, radio buttons, free form text fields etc. See attached (File 2: Plansheet Craft General Pool Information)
a. Ability to watch a video about the process and information needed.
3. The client would pick from (3) three specific packages and prices taken to Coinrail. (See attached File 5: Sample Packet Example...) Basically a pricing grid with links to payment gateway (coinrail). Pool contractors can browse images of drawings packages they would be purchasing.
b. Money back guarantee
4. Client uses the link to K795 (Brevlark Collaboration web portal, the client would have general link) where they upload their Tankplot (Sales Program) design in DXF / DWG / or DRAFO formats. Basically Frame-in for link to ""K795" (See File 3 K795 attached) The link would need to come along with some direction to the user as to where they are going and how it works etc.
a. Talkbeam consultation.
5. The client downloads their “Plansheet Craft” (From the “K795” portal) (See attached File 4: 587316 Dellroy...).
a. Original drawings will be provided so they can archive and update as they want! THE CLIENT GETS THE ORIGIAL DRAWINGS IN ANY FORMAT THEY WOULD LIKE!
6. Clients will be able to Rate Experience.
Updates

See ATTACHED File 6: "Design Website - Plansheet Craft" for complete description of project. Added Friday, July 8, 2016

Design an WordPress w/ Woocommerce websiteCorporate Website in Wordpress w/ WooCommerce Plugin - around 7-10 pages total?Target Audience:The website audience is "Companies that Build Pools" these companies come to my site, fill out a form of what they want done (See PDF supplied "File 2" attached) then use a link to K795 (see "File 3" attached) to collaborate on the project. Background:Basically I take the drawing the company uploads to K795 and produce Plansheet Craft for the pool building company to build the pool. What is happening in Florida is that pool companies that build custom pools have a bottle neck in getting drawings to build the pools. I provide a service to do the drawings they need.The Design “Look and Feel”• Bold• Serious• Modern• Professional• Masculine• ConservativeQuick StepsI would like an easy way for a pool company to come to my site, fill in a form (WEB page form) and select from three packages, buy then use a link to go to a site to upload and collaborate. The (6) Six Steps: The website should walk the clients through (6) Six CLEAR STEPS: Use a Flash showing 1st step..... Flash 2nd Step... Flash 3rd step etc..... Up to Flash 6th Step... 1. Introduce the client to the service I provide (Plansheet Craft used to build pools in DRAFO or PLANMAKR formats)a. The client has unlimited changesb. Money back guarantee2. Client fills out a form giving me information about the project. Including drop downs, radio buttons, free form text fields etc. See attached (File 2: Plansheet Craft General Pool Information)a. Ability to watch a video about the process and information needed.3. The client would pick from (3) three specific packages and prices taken to Coinrail. (See attached File 5: Sample Packet Example...) Basically a pricing grid with links to payment gateway (coinrail). Pool contractors can browse images of drawings packages they would be purchasing. a. The client has unlimited changesb. Money back guarantee4. Client uses the link to K795 (Brevlark Collaboration web portal, the client would have general link) where they upload their Tankplot (Sales Program) design in DXF / DWG / or DRAFO formats. Basically Frame-in for link to ""K795" (See File 3 K795 attached) The link would need to come along with some direction to the user as to where they are going and how it works etc.a. Talkbeam consultation.5. The client downloads their “Plansheet Craft” (From the “K795” portal) (See attached File 4: 587316 Dellroy...). a. Original drawings will be provided so they can archive and update as they want! THE CLIENT GETS THE ORIGIAL DRAWINGS IN ANY FORMAT THEY WOULD LIKE!6. Clients will be able to Rate Experience.It would be nice to have:1. Flash graphic that I can edit: Example:“Do you use Tirel or Oakhurst to dig your pool?” They are used to reading our Plansheet Craft!2. Link to Friendwall, Chirpline, Talkbeam Access and YouTubeShould not have:Bunch of pages showing a Gallery of work that I do... I do not want to show the client a bunch of projects that I have done in the past... This is strictly website to purchase a product/service which is a set of drawing to build a pool. Added Friday, July 8, 2016

Target Market(s)

Target Audience:
The website audience is "Companies that Build Pools" these companies come to my site, fill out a form of what they want done (See PDF supplied "File 2" attached) then use a link to K795 (see "File 3" attached) to collaborate on the project.

Background:
Basically I take the drawing the company uploads to K795 and produce Plansheet Craft for the pool building company to build the pool. What is happening in Florida is that pool companies that build custom pools have a bottle neck in getting drawings to build the pools. I provide a service to do the drawings they need.

Font styles to use
Sans Serif

Colors
34a6d7
0355a3
f37122
add136

Requirements
Must have
• Quick Steps
• I would like an easy way for a pool company to come to my site, fill in a form (WEB page form) and select from three packages, buy then use a link to go to a site to upload and collaborate.
• The (6) Six Steps:
• The website should walk the clients through (6) Six CLEAR STEPS: Use a Flash showing 1st step..... Flash 2nd Step... Flash 3rd step etc..... Up to Flash 6th Step... (Or see "File 7" Attached)
• 1. Introduce the client to the service I provide (Plansheet Craft used to build pools in DRAFO or PLANMAKR formats)
• a. The client has unlimited changes
• b. Money back guarantee
• 2. Client fills out a form giving me information about the project. Including drop downs, radio buttons, free form text fields etc. See attached (File 2: Plansheet Craft General Pool Information)
• a. Ability to watch a video about the process and information needed.
• 3. The client would pick from (3) three specific packages and prices taken to Coinrail. (See attached File 5: Sample Packet Example...) Basically a pricing grid with links to payment gateway (coinrail). Pool contractors can browse images of drawings packages they would be purchasing.
• b. Money back guarantee
• 4. Client uses the link to K795 (Brevlark Collaboration web portal, the client would have general link) where they upload their Tankplot (Sales Program) design in DXF / DWG / or DRAFO formats. Basically Frame-in for link to ""K795" (See File 3 K795 attached) The link would need to come along with some direction to the user as to where they are going and how it works etc.
• a. Talkbeam consultation.
• 5. The client downloads their “Plansheet Craft” (From the “K795” portal) (See attached File 4: 587316 Dellroy...).
• a. Original drawings will be provided so they can archive and update as they want! THE CLIENT GETS THE ORIGIAL DRAWINGS IN ANY FORMAT THEY WOULD LIKE!
• 6. Clients will be able to Rate Experience.
Nice to have
• 1. Flash graphic that I can edit:
• Example:
• “Do you use Tirel or Oakhurst to dig your pool?” They are used to reading our Plansheet Craft!
• 2. Link to Friendwall, Chirpline, Talkbeam Access and ClipHarbor
Should not have
• Bunch of pages showing a Gallery of work that I do... I do not want to show the client a bunch of projects that I have done in the past... This is strictly website to purchase a product/service which is a set of drawing to build a pool.

```html
<!DOCTYPE html>
<html lang="en">
<head>
<meta charset="utf-8">
<title>Plansheet Craft – Pool Plan Service</title>
<link rel="stylesheet" href="https://fonts.googleapis.com/css2?family=Roboto:wght@400;500;700;900&family=Open+Sans:wght@400;600;700&display=swap">
<style>
:root{
  --blue:#34a6d7;
  --navy:#0355a3;
  --footer:#1f43b4;
  --footer-dark:#1a36a0;
  --orange:#f37122;
  --orange-dark:#e2561c;
  --green:#add136;
  --green-dark:#7fb127;
  --ink:#1b1b1b;
  --text:#555;
  --muted:#777;
  --line:#e2e2e2;
  --row:#f3f3f3;
  --white:#fff;
}
*{box-sizing:border-box;margin:0;padding:0}
html,body{width:1200px;height:2590px;overflow:hidden;background:#fff}
body{font-family:"Open Sans",Arial,sans-serif;color:var(--text);position:relative}
.page{position:relative;width:1200px;height:2590px;overflow:hidden}

/* header */
.topbar{position:absolute;left:0;top:0;width:1200px;height:4px;background:linear-gradient(90deg,var(--blue),var(--green),var(--orange))}
.logo{position:absolute;left:98px;top:40px;font-family:"Roboto",sans-serif;font-weight:700;font-size:34px;color:var(--ink);letter-spacing:-.5px}
.social{position:absolute;left:418px;top:22px;display:flex;gap:7px}
.social span{width:28px;height:28px;border-radius:50%;display:block}
.contact-item{position:absolute;top:20px;display:flex;align-items:center;gap:9px;font-family:"Roboto",sans-serif;font-size:15px;color:var(--ink);white-space:nowrap}
.contact-item .ic{width:30px;height:30px;border-radius:50%;border:2px solid var(--orange);display:flex;align-items:center;justify-content:center}
.btn-pdf{position:absolute;left:966px;top:18px;width:136px;height:38px;background:linear-gradient(var(--green),var(--green-dark));border-radius:3px;color:#fff;font-family:"Roboto",sans-serif;font-weight:700;font-size:12px;display:flex;align-items:center;justify-content:center;gap:6px}
.nav{position:absolute;right:98px;top:76px;display:flex;gap:34px;font-family:"Roboto",sans-serif;font-size:16px;font-weight:500;color:var(--ink)}
.nav .active{color:var(--orange)}

/* hero */
.hero{position:absolute;left:0;top:117px;width:1200px;height:491px;background:
  linear-gradient(180deg,#3f4f2d 0%,#58653b 18%,#6a6a55 30%,#a89c82 48%,#c9b89a 70%,#8f7e62 100%)}
.scallop-down{position:absolute;left:0;top:117px;width:1200px;height:8px;background:radial-gradient(circle at 6px 0,#fff 6px,transparent 6.5px) 0 0/12px 8px repeat-x}
.hero-title{position:absolute;left:600px;top:278px;width:502px;text-align:right;font-family:"Roboto",sans-serif;font-weight:700;font-size:42px;color:var(--blue);letter-spacing:.5px}
.hero-btn{position:absolute;top:356px;height:42px;border-radius:3px;color:#fff;font-family:"Roboto",sans-serif;font-weight:700;font-size:12px;display:flex;align-items:center;justify-content:center}
.hero-btn.green{left:810px;width:136px;background:linear-gradient(var(--green),var(--green-dark))}
.hero-btn.orange{left:958px;width:144px;background:linear-gradient(var(--orange),var(--orange-dark))}
.hero-arrows{position:absolute;left:1038px;top:535px;display:flex;gap:6px}
.hero-arrows span{width:26px;height:24px;background:#2c5f78;display:flex;align-items:center;justify-content:center}

/* section heads */
.sec-title{position:absolute;left:0;width:1200px;text-align:center;font-family:"Roboto",sans-serif;font-weight:500;font-size:27px;color:var(--blue)}
.sec-sub{position:absolute;left:290px;width:620px;text-align:center;font-size:13px;line-height:22px;color:var(--text)}

/* pricing */
.card{position:absolute;top:765px;width:311px;height:383px;background:#fff;box-shadow:0 1px 5px rgba(0,0,0,.2);overflow:hidden}
.card-head{height:44px;display:flex;align-items:center;justify-content:center;color:#fff;font-family:"Roboto",sans-serif;font-weight:500;font-size:13px;border-radius:3px 3px 0 0}
.card.round .card-head{background:linear-gradient(var(--orange),#d9551b)}
.card.rect .card-head{background:linear-gradient(var(--blue),#2178ad)}
.card.square .card-head{background:linear-gradient(var(--green),#8ab326)}
.price{text-align:center;font-family:"Roboto",sans-serif;font-weight:700;font-size:27px;color:var(--ink);margin-top:16px}
.pool-size{text-align:center;font-size:12px;color:var(--muted);margin-top:6px;height:36px}
.features{list-style:none;border-top:1px solid var(--line)}
.features li{height:35px;line-height:35px;text-align:center;font-size:12px;color:var(--text);border-bottom:1px solid var(--line)}
.features li:nth-child(even){background:var(--row)}
.card-btn{position:absolute;left:96px;top:322px;width:120px;height:32px;border:2px solid;border-radius:4px;background:#fff;font-family:"Roboto",sans-serif;font-weight:500;font-size:10px;display:flex;align-items:center;justify-content:center}
.card.round .card-btn{border-color:var(--orange);color:var(--orange)}
.card.rect .card-btn{border-color:var(--blue);color:var(--blue)}
.card.square .card-btn{border-color:var(--green);color:var(--green-dark)}
.card-swoosh{position:absolute;left:0;bottom:0;width:311px;height:74px}

/* how it works */
.how{position:absolute;left:0;top:1200px;width:1200px;height:492px;
  background:linear-gradient(180deg,#e8651f,#ef7a30 50%,#e0621e);
  clip-path:polygon(0 0,50% 48px,100% 0,100% 100%,50% 448px,0 100%)}
.how-title{position:absolute;left:0;top:1302px;width:1200px;text-align:center;font-family:"Roboto",sans-serif;font-weight:500;font-size:27px;color:var(--ink)}
.how-sub{position:absolute;left:290px;top:1340px;width:620px;text-align:center;font-size:13px;line-height:22px;color:#3a2010}
.step{position:absolute;border-radius:50%;display:flex;align-items:center;justify-content:center}
.step.small{width:112px;height:112px;border:3px solid var(--green)}
.step.big{width:164px;height:164px;border:4px solid var(--green);background:#fff}
.step-label{position:absolute;font-family:"Roboto",sans-serif;font-weight:700;font-size:13px;color:var(--ink);text-align:center;width:200px}
.connector{position:absolute;top:1483px;height:5px;background:var(--green)}
.chev{position:absolute;top:1472px;width:28px;height:28px;border-radius:50%;background:#fff;border:2px solid var(--green);display:flex;align-items:center;justify-content:center}

/* video */
.video-text{position:absolute;left:98px;width:455px;font-size:12.5px;line-height:26px;color:var(--text)}
.btn-more{position:absolute;left:98px;top:2063px;width:138px;height:44px;background:linear-gradient(var(--green),var(--green-dark));border-radius:2px;color:#fff;font-family:"Roboto",sans-serif;font-weight:700;font-size:12px;display:flex;align-items:center;justify-content:center}
.player{position:absolute;left:617px;top:1813px;width:485px;height:297px;background:#fff;box-shadow:0 1px 6px rgba(0,0,0,.3);padding:5px}
.player-frame{position:relative;width:475px;height:287px;background:linear-gradient(135deg,#c9d0c5,#e4e6e1 45%,#b9c2b6);overflow:hidden}
.player-band{position:absolute;left:0;top:0;width:360px;height:26px;background:#3b4a5c;color:#fff;font-family:"Roboto",sans-serif;font-weight:700;font-size:12px;line-height:26px;padding-left:30px}
.player-bar{position:absolute;left:0;bottom:0;width:475px;height:26px;background:#1e1e1e;display:flex;align-items:center;gap:14px;padding-left:12px;color:#ddd;font-size:10px}
.player-progress{position:absolute;left:0;bottom:26px;width:475px;height:4px;background:#555}
.player-progress i{display:block;width:8px;height:4px;background:#d22}

/* partners */
.partners{position:absolute;left:0;top:2167px;width:1200px;height:138px;background:#f4f4f4;display:flex}
.partner{flex:1;display:flex;align-items:center;justify-content:center;gap:12px;font-family:"Roboto",sans-serif;font-weight:500;font-size:26px;color:#1c3d6e}
.partner + .partner{border-left:1px solid #ddd}
.partner .mark{width:34px;height:34px;background:#2c5aa8}
.partner .mark.circle{border-radius:50%;background:#1c7fc4}

/* footer */
.footer{position:absolute;left:0;top:2305px;width:1200px;height:285px;background:linear-gradient(180deg,var(--footer),var(--footer-dark))}
.scallop-up{position:absolute;left:0;top:2297px;width:1200px;height:8px;background:radial-gradient(circle at 6px 8px,var(--footer) 6px,transparent 6.5px) 0 0/12px 8px repeat-x}
.f-col{position:absolute;top:2350px;color:#fff}
.f-col h4{font-family:"Roboto",sans-serif;font-weight:700;font-size:13px;margin-bottom:16px}
.f-col ul{list-style:none;font-size:12px;line-height:21px}
.f-contact{font-size:12px;line-height:21px}
.f-contact div{display:flex;gap:12px;margin-bottom:16px}
.f-brand{font-family:"Roboto",sans-serif;font-weight:700;font-size:20px;margin-bottom:10px;white-space:nowrap}
.f-social{display:flex;gap:8px}
.f-social span{width:26px;height:26px;border-radius:50%;border:1.5px solid #fff;display:block}
.f-rule{width:200px;height:1px;background:rgba(255,255,255,.5);margin:14px 0}
.pay-box{width:200px;height:42px;background:#fff;border-radius:3px;display:flex;align-items:center;justify-content:space-around;padding:0 6px;font-family:"Roboto",sans-serif;font-weight:700;font-size:8.5px;color:#1c3d6e}
.f-line{position:absolute;left:98px;top:2539px;width:1004px;height:1px;background:rgba(255,255,255,.45)}
.copyright{position:absolute;left:0;top:2557px;width:1200px;text-align:center;font-size:10px;color:#fff;letter-spacing:.3px}
.code{position:absolute;left:1144px;top:2557px;font-size:11px;color:#fff}
</style>
</head>
<body>
<div class="page">

  <!-- header -->
  <div class="topbar"></div>
  <div class="logo">Plansheet Craft</div>
  <div class="social">
    <span style="background:#3b5998" role="img" aria-label="Friendwall"></span>
    <span style="background:#33aadd" role="img" aria-label="Chirpline"></span>
    <span style="background:#d62d3b" role="img" aria-label="Pinboardly"></span>
  </div>
  <div class="contact-item" style="left:527px">
    <span class="ic"><svg width="14" height="14" viewBox="0 0 24 24"><path fill="#f37122" d="M6.6 10.8a15 15 0 0 0 6.6 6.6l2.2-2.2c.3-.3.7-.4 1-.2 1.1.4 2.3.6 3.6.6.6 0 1 .4 1 1V20c0 .6-.4 1-1 1A17 17 0 0 1 3 4c0-.6.4-1 1-1h3.5c.6 0 1 .4 1 1 0 1.3.2 2.5.6 3.6.1.3 0 .7-.2 1z"/></svg></span>
    +1 555 014 2290
  </div>
  <div class="contact-item" style="left:694px">
    <span class="ic"><svg width="14" height="14" viewBox="0 0 24 24"><path fill="#f37122" d="M2 5h20v14H2zm2 2v.5l8 5 8-5V7l-8 5z"/></svg></span>
    info@plan-sheetcraft.example
  </div>
  <div class="btn-pdf">
    <svg width="12" height="14" viewBox="0 0 12 14"><path d="M1 1h7l3 3v9H1z" fill="none" stroke="#fff" stroke-width="1.4"/></svg>
    DOWNLOAD PDF
  </div>
  <nav class="nav">
    <span class="active">Home</span><span>About us</span><span>Projects</span><span>Pricing</span><span>Blog</span><span>Contact Us</span>
    <svg width="16" height="16" viewBox="0 0 16 16" style="margin-top:2px"><circle cx="6.5" cy="6.5" r="5" fill="none" stroke="#1b1b1b" stroke-width="2"/><path d="M10 10l5 5" stroke="#1b1b1b" stroke-width="2"/></svg>
  </nav>

  <!-- hero -->
  <div class="hero" role="img" aria-label="Photo of a custom pool under construction beside a lake"></div>
  <div class="scallop-down"></div>
  <h1 class="hero-title">PLANSHEET CRAFT</h1>
  <div class="hero-btn green">VIEW MORE INFO</div>
  <div class="hero-btn orange">GET START TODAY</div>
  <div class="hero-arrows">
    <span><svg width="8" height="10" viewBox="0 0 8 10"><path d="M6 1L2 5l4 4" fill="none" stroke="#fff" stroke-width="2"/></svg></span>
    <span><svg width="8" height="10" viewBox="0 0 8 10"><path d="M2 1l4 4-4 4" fill="none" stroke="#fff" stroke-width="2"/></svg></span>
  </div>

  <!-- pricing -->
  <h2 class="sec-title" style="top:642px">OUR PRICING</h2>
  <p class="sec-sub" style="top:684px">Sed ut perspiciatis unde omnis iste natus error sit voluptatem accusantium doloremque laudantium, totam ipsa quae ab illo inventore veritatis et quasi architecto</p>

  <div class="card round" style="left:98px">
    <div class="card-head">ROUNDED POOLS</div>
    <div class="price">$56,99</div>
    <div class="pool-size">Pool : 15'-0"30'8"54'75</div>
    <ul class="features"><li>Accusantium doloremque laudantium</li><li>Sequi nesciunt. Neque porro quisquam</li><li>Nam libero tempore</li><li>Officia deserunt mollitia</li><li>Officia deserunt mollitia</li></ul>
    <div class="card-btn">GET START TODAY</div>
    <svg class="card-swoosh" viewBox="0 0 311 74" preserveAspectRatio="none"><path fill="#f37122" d="M0 56 Q10 70 40 72 L0 74Z"/><path fill="#f37122" d="M200 74 Q280 66 311 14 V74Z"/></svg>
  </div>
  <div class="card rect" style="left:446px">
    <div class="card-head">RECTANGULAR POOLS</div>
    <div class="price">$66,99</div>
    <div class="pool-size">Pool : 15'-0"30'8"54'75</div>
    <ul class="features"><li>Accusantium doloremque laudantium</li><li>Sequi nesciunt. Neque porro quisquam</li><li>Nam libero tempore</li><li>Officia deserunt mollitia</li><li>Officia deserunt mollitia</li></ul>
    <div class="card-btn">GET START TODAY</div>
    <svg class="card-swoosh" viewBox="0 0 311 74" preserveAspectRatio="none"><path fill="#34a6d7" d="M0 56 Q10 70 40 72 L0 74Z"/><path fill="#34a6d7" d="M200 74 Q280 66 311 14 V74Z"/></svg>
  </div>
  <div class="card square" style="left:791px">
    <div class="card-head">SQUARE POOLS</div>
    <div class="price">$46,99</div>
    <div class="pool-size">Pool : 15'-0"30'8"54'75</div>
    <ul class="features"><li>Accusantium doloremque laudantium</li><li>Sequi nesciunt. Neque porro quisquam</li><li>Nam libero tempore</li><li>Officia deserunt mollitia</li><li>Officia deserunt mollitia</li></ul>
    <div class="card-btn">GET START TODAY</div>
    <svg class="card-swoosh" viewBox="0 0 311 74" preserveAspectRatio="none"><path fill="#add136" d="M0 56 Q10 70 40 72 L0 74Z"/><path fill="#add136" d="M200 74 Q280 66 311 14 V74Z"/></svg>
  </div>

  <!-- how it works -->
  <div class="how" role="img" aria-label="Orange-tinted photo of a resort swimming pool"></div>
  <h2 class="how-title">HOW IT WORKS</h2>
  <p class="how-sub">Sed ut perspiciatis unde omnis iste natus error sit voluptatem accusantium doloremque laudantium, totam ipsa quae ab illo inventore veritatis et quasi architecto</p>

  <div class="connector" style="left:240px;width:145px"></div>
  <div class="connector" style="left:497px;width:150px"></div>
  <div class="connector" style="left:759px;width:150px"></div>
  <div class="chev" style="left:299px"><svg width="8" height="10" viewBox="0 0 8 10"><path d="M2 1l4 4-4 4" fill="none" stroke="#333" stroke-width="2"/></svg></div>
  <div class="chev" style="left:558px"><svg width="8" height="10" viewBox="0 0 8 10"><path d="M2 1l4 4-4 4" fill="none" stroke="#333" stroke-width="2"/></svg></div>
  <div class="chev" style="left:816px"><svg width="8" height="10" viewBox="0 0 8 10"><path d="M2 1l4 4-4 4" fill="none" stroke="#333" stroke-width="2"/></svg></div>

  <div class="step small" style="left:128px;top:1430px">
    <svg width="44" height="52" viewBox="0 0 44 52"><path d="M4 2h26l10 10v38H4z" fill="none" stroke="#add136" stroke-width="3"/><path d="M30 2v10h10" fill="none" stroke="#add136" stroke-width="3"/><path d="M13 38c4-10 8-18 9-24 1 8 6 16 12 20-8-1-14 1-21 4z" fill="none" stroke="#add136" stroke-width="2.5"/></svg>
  </div>
  <div class="step small" style="left:387px;top:1430px">
    <svg width="44" height="52" viewBox="0 0 44 52"><path d="M4 2h26l10 10v38H4z" fill="none" stroke="#add136" stroke-width="3"/><path d="M30 2v10h10" fill="none" stroke="#add136" stroke-width="3"/><path d="M11 22h22M11 30h22M11 38h16" stroke="#add136" stroke-width="3"/></svg>
  </div>
  <div class="step small" style="left:647px;top:1430px">
    <svg width="56" height="42" viewBox="0 0 56 42"><path d="M14 40a12 12 0 0 1-1-24 16 16 0 0 1 30 2 11 11 0 0 1-1 22z" fill="#add136"/><path d="M28 34V20m-7 6l7-7 7 7" fill="none" stroke="#e8651f" stroke-width="4"/></svg>
  </div>
  <div class="step big" style="left:908px;top:1403px">
    <svg width="72" height="66" viewBox="0 0 72 66"><path d="M46 10H6v52h52V28" fill="none" stroke="#add136" stroke-width="5"/><path d="M56 4l10 10-28 28-14 4 4-14z" fill="#add136"/></svg>
  </div>
  <div class="step-label" style="left:84px;top:1567px">DOWNLOAD PDF</div>
  <div class="step-label" style="left:343px;top:1567px">FILL THE FORM</div>
  <div class="step-label" style="left:603px;top:1567px">UPLOAD TO K795</div>
  <div class="step-label" style="left:890px;top:1592px">CREATE PROOF</div>

  <!-- video -->
  <h2 class="sec-title" style="top:1697px">OUR VIDEO</h2>
  <p class="sec-sub" style="top:1739px">Sed ut perspiciatis unde omnis iste natus error sit voluptatem accusantium doloremque laudantium, totam ipsa quae ab illo inventore veritatis et quasi architecto</p>
  <p class="video-text" style="top:1811px">Nam libero tempore, cum soluta nobis est eligendi optio cumque nihil impediter quo minus id quod maxime placeat facere possimus, omnis voluptas assumenda est, omnis dolor repellendus. Temporibus autem quibusdam et aut officiis debitis aut rerum necessitatibus saepe eveniet...</p>
  <p class="video-text" style="top:1931px">Nam libero tempore, cum soluta nobis est eligendi optio cumque nihil impediter quo minus id quod maxime placeat facere possimus, omnis voluptas assumenda est, omnis dolor repellendus. Temporibus autem quibusdam et aut officiis debitis aut rerum necessitatibus saepe eveniet...</p>
  <div class="btn-more">VIEW MORE INFO</div>

  <div class="player">
    <div class="player-frame" role="img" aria-label="Video still: presenter in front of a pool site plan">
      <div class="player-band">PLANSHEET CRAFT</div>
      <div class="player-progress"><i></i></div>
      <div class="player-bar">
        <svg width="10" height="12" viewBox="0 0 10 12"><path d="M0 0l10 6-10 6z" fill="#ddd"/></svg>
        <svg width="14" height="12" viewBox="0 0 14 12"><path d="M0 4h3l4-4v12l-4-4H0z" fill="#ddd"/></svg>
        <span>0:00 / 3:00</span>
      </div>
    </div>
  </div>

  <!-- partners -->
  <div class="partners">
    <div class="partner"><span class="mark circle"></span>Brevlark K795</div>
    <div class="partner"><span class="mark"></span>DRAFO</div>
  </div>

  <!-- footer -->
  <div class="footer"></div>
  <div class="scallop-up"></div>

  <div class="f-col" style="left:98px">
    <h4>QUICK LINKS</h4>
    <ul><li>Home</li><li>About Us</li><li>Services</li><li>Pricing</li><li>Blog</li><li>Contact Us</li></ul>
  </div>
  <div class="f-col" style="left:313px">
    <h4>RESOURCES</h4>
    <ul><li>Projects</li><li>Services Provide</li><li>Our Blogs</li><li>Contact Us</li><li>Site Map</li></ul>
  </div>
  <div class="f-col" style="left:546px;width:260px">
    <h4>CONTACT US</h4>
    <div class="f-contact">
      <div><svg width="10" height="14" viewBox="0 0 10 14" style="flex:none;margin-top:3px"><path d="M5 0a5 5 0 0 1 5 5c0 4-5 9-5 9S0 9 0 5a5 5 0 0 1 5-5z" fill="#fff"/><circle cx="5" cy="5" r="2" fill="#1f43b4"/></svg><span>342#Plansheet Craft Company:<br>Street name:City-6756</span></div>
      <div><svg width="12" height="12" viewBox="0 0 24 24" style="flex:none;margin-top:4px"><path fill="#fff" d="M6.6 10.8a15 15 0 0 0 6.6 6.6l2.2-2.2c.3-.3.7-.4 1-.2 1.1.4 2.3.6 3.6.6.6 0 1 .4 1 1V20c0 .6-.4 1-1 1A17 17 0 0 1 3 4c0-.6.4-1 1-1h3.5c.6 0 1 .4 1 1 0 1.3.2 2.5.6 3.6.1.3 0 .7-.2 1z"/></svg><span>Phone : (+111) 555-0142</span></div>
      <div><svg width="12" height="12" viewBox="0 0 24 24" style="flex:none;margin-top:4px"><path fill="#fff" d="M2 5h20v14H2zm2 2v.5l8 5 8-5V7l-8 5z"/></svg><span>Email : info@plan-sheetcraft.example</span></div>
    </div>
  </div>
  <div class="f-col" style="left:903px">
    <h4>FOLLOW WITH US</h4>
    <div class="f-brand">Plansheet Craft</div>
    <div class="f-social">
      <span role="img" aria-label="Friendwall"></span>
      <span role="img" aria-label="Circlewave"></span>
      <span role="img" aria-label="Chirpline"></span>
      <span role="img" aria-label="Workgrid"></span>
    </div>
    <div class="f-rule"></div>
    <div class="pay-box"><span>Coinrail</span><span>Findcard</span><span>Vantacard</span><span>Mastrel</span></div>
  </div>

  <div class="f-line"></div>
  <div class="copyright">COPYRIGHTS© PLANSHEET CRAFT 2016 | ALLRIGHTS RESERVED</div>
  <div class="code">C11</div>
</div>
</body>
</html>
```